Global Expert Network Firm needs business card design

We need business card design for a new company based in Seoul, South Korea called 'Corwell Insight Partners'. We recruit industry experts covering all countries and connect our client and recruited expert by phone, face-to-face meetings and etc. We are a global expert network firm that is focused on delivering high-quality experts to our clients throughout the world. Our clients include multinational corporations, global consulting firms, private equity firms, venture capital firms, asset management companies.
We have made new logo and please find attachment.(Please use new logo)
Target Market(s)
Global Consulting Firms, Investment Firms, Private Equity Firms, Venture Capital Firms.
Industry/Entity Type
Recruitment
Contact Information for Business Card
We need two Languages (English and Korean Version).
The front is Korean and the back is English version.
[The back] [English]
Company Name: Corwell Insight Partners, Inc.
CEO Name: Daniel Park
Address: #507, Hanbit Bldg, 82 Maebongsan-ro, Dobong-gu, Seoul, 01327, Korea
Tel. +82 2 718 4052
Fax. +82 2 864 1097
Mobile. +82 10 7264 8815
Email: daniel@corwellip.com
Web: www.corwellip.com
[The front] [Korean] => Described in same order as English version.
회사명: 코웰인사이트파트너스(주)
대표이사: 박도현
주소: 서울시 도봉구 매봉산로 82 한빛빌딩 507호
Tel. 02 718 4052
Fax. 02 864 1097
Mobile. 010 7264 8815
Web: www.corwellip.com
Look and feel
Each slider illustrates characteristics of the customer's brand and the style your logo design should communicate.

```html
<!DOCTYPE html>
<html lang="en">
<head>
<meta charset="utf-8">
<title>Corwell Insight Partners — Business Cards</title>
<link rel="stylesheet" href="https://fonts.googleapis.com/css2?family=Lato:wght@400;700&family=Noto+Sans+KR:wght@300;400;500&display=swap">
<style>
  :root {
    --stage: #2a2c31;
    --paper: #ffffff;
    --navy: #26296b;
    --ink: #141416;
    --tab-grey: #c4c5c8;
    --text-light: #ffffff;
    --text-soft: #d9dbe6;
  }
  * { box-sizing: border-box; margin: 0; padding: 0; }
  html, body { width: 1200px; height: 900px; overflow: hidden; }
  body {
    background: var(--stage);
    font-family: "Lato", "Noto Sans KR", sans-serif;
    position: relative;
  }
  .card {
    position: absolute;
    left: 300px;
    width: 600px;
    height: 343px;
    border-radius: 24px;
    overflow: hidden;
    background: var(--paper);
    box-shadow: 0 10px 30px rgba(0,0,0,.45);
  }
  .card--front { top: 66px; }
  .card--back { top: 486px; }
  .card-shapes { position: absolute; inset: 0; width: 100%; height: 100%; }

  .brand-box {
    position: absolute;
    left: 150px; top: 16px;
    width: 132px; height: 112px;
    background: var(--navy);
    display: flex; align-items: center; justify-content: center;
    padding: 10px;
  }
  .brand-name {
    color: var(--text-soft);
    font-family: "Lato", sans-serif;
    font-weight: 400;
    font-size: 17px;
    line-height: 1.25;
    letter-spacing: .5px;
  }
  .card--front .brand-name {
    font-family: "Noto Sans KR", sans-serif;
    font-weight: 300;
    font-size: 17px;
    line-height: 1.4;
  }

  .contact {
    position: absolute;
    display: flex; align-items: flex-start; gap: 7px;
    color: var(--text-light);
    font-size: 12.5px;
    line-height: 1.35;
    white-space: nowrap;
  }
  .card--front .contact { font-family: "Noto Sans KR", "Lato", sans-serif; }
  .contact .num { font-family: "Lato", sans-serif; }
  .contact svg { width: 12px; height: 12px; flex: none; margin-top: 2px; fill: var(--text-light); }
  .contact--address { left: 40px; top: 150px; }
  .contact--tel { left: 40px; top: 194px; }
  .contact--mobile { left: 40px; top: 218px; }
  .contact--fax { left: 210px; top: 218px; }
  .contact--email { left: 210px; top: 242px; }
  .contact--web { left: 370px; top: 300px; font-size: 14px; }

  .name-tag {
    position: absolute;
    left: 392px; top: 200px;
    width: 180px; height: 64px;
    color: var(--text-light);
    padding: 10px 18px;
  }
  .person-name {
    font-size: 19px; font-weight: 700; letter-spacing: .3px; line-height: 1.2;
  }
  .person-title { font-size: 12px; color: var(--text-soft); margin-top: 3px; }
  .card--front .person-name { font-family: "Noto Sans KR", sans-serif; font-weight: 500; font-size: 20px; }
  .card--front .person-title { font-family: "Noto Sans KR", sans-serif; }
</style>
</head>
<body>

<svg width="0" height="0" style="position:absolute" aria-hidden="true">
  <defs>
    <symbol id="icon-pin" viewBox="0 0 24 24"><path d="M12 2a7 7 0 0 0-7 7c0 5 7 13 7 13s7-8 7-13a7 7 0 0 0-7-7zm0 9.5A2.5 2.5 0 1 1 12 6.5a2.5 2.5 0 0 1 0 5z"/></symbol>
    <symbol id="icon-phone" viewBox="0 0 24 24"><path d="M6.6 10.8a15 15 0 0 0 6.6 6.6l2.2-2.2a1 1 0 0 1 1-.25 11.4 11.4 0 0 0 3.6.57 1 1 0 0 1 1 1V20a1 1 0 0 1-1 1A17 17 0 0 1 3 4a1 1 0 0 1 1-1h3.5a1 1 0 0 1 1 1c0 1.25.2 2.45.57 3.6a1 1 0 0 1-.25 1z"/></symbol>
    <symbol id="icon-mobile" viewBox="0 0 24 24"><path d="M7 2h10a2 2 0 0 1 2 2v16a2 2 0 0 1-2 2H7a2 2 0 0 1-2-2V4a2 2 0 0 1 2-2zm0 3v13h10V5z"/></symbol>
    <symbol id="icon-fax" viewBox="0 0 24 24"><path d="M6 2h12v6H6zM4 9h16a2 2 0 0 1 2 2v7h-4v4H6v-4H2v-7a2 2 0 0 1 2-2zm4 8v3h8v-3z"/></symbol>
    <symbol id="icon-mail" viewBox="0 0 24 24"><path d="M2 5h20v14H2zm2 2v.5l8 5 8-5V7z"/></symbol>
    <symbol id="icon-globe" viewBox="0 0 24 24"><path d="M12 2a10 10 0 1 0 0 20 10 10 0 0 0 0-20zm6.9 6h-3a15 15 0 0 0-1.3-3.6A8 8 0 0 1 18.9 8zM12 4c.8 1.1 1.5 2.5 1.9 4h-3.8c.4-1.5 1.1-2.9 1.9-4zM4.3 14a8 8 0 0 1 0-4h3.4a16 16 0 0 0 0 4zm.8 2h3a15 15 0 0 0 1.3 3.6A8 8 0 0 1 5.1 16zm3-8h-3a8 8 0 0 1 4.3-3.6A15 15 0 0 0 8.1 8zM12 20c-.8-1.1-1.5-2.5-1.9-4h3.8c-.4 1.5-1.1 2.9-1.9 4zm2.3-6H9.7a14 14 0 0 1 0-4h4.6a14 14 0 0 1 0 4zm.3 5.6a15 15 0 0 0 1.3-3.6h3a8 8 0 0 1-4.3 3.6zM16.3 14a16 16 0 0 0 0-4h3.4a8 8 0 0 1 0 4z"/></symbol>
  </defs>
</svg>

<!-- Korean side -->
<section class="card card--front" lang="ko">
  <svg class="card-shapes" viewBox="0 0 600 343" preserveAspectRatio="none" aria-hidden="true">
    <path fill="var(--navy)" d="M0,140 H330 Q350,140 362,160 L405,250 H600 V343 H0 Z"/>
    <path fill="var(--ink)" d="M0,172 H310 Q330,172 340,190 L375,255 Q382,268 400,268 H440 Q470,268 490,220 L505,195 Q512,185 525,185 H600 V343 H0 Z"/>
    <path fill="var(--tab-grey)" d="M398,182 Q400,172 410,172 H452 L430,212 H392 Z"/>
    <path fill="var(--navy)" d="M400,200 H552 Q572,200 572,220 V264 H410 Q392,264 392,246 Z"/>
  </svg>
  <div class="brand-box"><span class="brand-name">코웰인사이트<br>파트너스(주)</span></div>
  <div class="contact contact--address"><svg><use href="#icon-pin"/></svg><span>서울시 도봉구 매봉산로 82 한빛빌딩 507호</span></div>
  <div class="contact contact--tel"><svg><use href="#icon-phone"/></svg><span class="num">+82 2 718 4052</span></div>
  <div class="contact contact--mobile"><svg><use href="#icon-mobile"/></svg><span class="num">+82 10 7264 8815</span></div>
  <div class="contact contact--fax"><svg><use href="#icon-fax"/></svg><span class="num">+82 2 864 1097</span></div>
  <div class="contact contact--email"><svg><use href="#icon-mail"/></svg><span class="num">daniel@corwellip.com</span></div>
  <div class="contact contact--web"><svg><use href="#icon-globe"/></svg><span class="num">www.corwellip.com</span></div>
  <div class="name-tag">
    <div class="person-name">박도현</div>
    <div class="person-title">대표이사</div>
  </div>
</section>

<!-- English side -->
<section class="card card--back" lang="en">
  <svg class="card-shapes" viewBox="0 0 600 343" preserveAspectRatio="none" aria-hidden="true">
    <path fill="var(--navy)" d="M0,140 H330 Q350,140 362,160 L405,250 H600 V343 H0 Z"/>
    <path fill="var(--ink)" d="M0,172 H310 Q330,172 340,190 L375,255 Q382,268 400,268 H440 Q470,268 490,220 L505,195 Q512,185 525,185 H600 V343 H0 Z"/>
    <path fill="var(--tab-grey)" d="M398,182 Q400,172 410,172 H452 L430,212 H392 Z"/>
    <path fill="var(--navy)" d="M400,200 H552 Q572,200 572,220 V264 H410 Q392,264 392,246 Z"/>
  </svg>
  <div class="brand-box"><span class="brand-name">CORWELL<br>INSIGHT<br>PARTNERS</span></div>
  <div class="contact contact--address"><svg><use href="#icon-pin"/></svg><span>#507, Hanbit Bldg, 82 Maebongsan-ro,<br>Dobong-gu, Seoul, 01327, Korea</span></div>
  <div class="contact contact--tel" style="top:200px"><svg><use href="#icon-phone"/></svg><span>+82 2 718 4052</span></div>
  <div class="contact contact--mobile" style="top:224px"><svg><use href="#icon-mobile"/></svg><span>+82 10 7264 8815</span></div>
  <div class="contact contact--fax" style="top:224px"><svg><use href="#icon-fax"/></svg><span>+82 2 864 1097</span></div>
  <div class="contact contact--email" style="top:248px"><svg><use href="#icon-mail"/></svg><span>daniel@corwellip.com</span></div>
  <div class="contact contact--web"><svg><use href="#icon-globe"/></svg><span>www.corwellip.com</span></div>
  <div class="name-tag">
    <div class="person-name">DANIEL PARK</div>
    <div class="person-title">CEO</div>
  </div>
</section>

</body>
</html>
```